Product Label with Company Logo & Product Information

I am looking for a new label design for one of my products, Candied Pecans. I am including an old label that I made, but it does not "pop" on the current packaging. See image of current packaging attached as well.

I want the design to ultimately be something that I can take and order a roll of labels/stickers. Please stick within standard label/sticker sizes (round or square). Please include final size as well.

Must Haves:
(1) Company logo (any color variation-see attached logo images).
(2) All wording on the old label
(3) Label size can not be more than 2 in. x 4 in. (I would actually like them a little smaller). They seem kind of big as they are right now.

```html
<!DOCTYPE html>
<html lang="en">
<head>
<meta charset="utf-8">
<title>Gourmet Candied Pecans – Label Options</title>
<link href="https://fonts.googleapis.com/css2?family=Federo&family=Fraunces:opsz,wght@9..144,700&family=DM+Serif+Display&family=Tinos&family=Lexend:wght@600;700&display=swap" rel="stylesheet">
<style>
  :root {
    --bg: #ebebeb;
    --paper: #ffffff;
    --lemon: #f9ec28;
    --lemon-soft: #fdf8c8;
    --ink: #545454;
    --ink-dark: #222222;
  }
  * { box-sizing: border-box; margin: 0; padding: 0; }
  html, body { width: 1200px; height: 1200px; overflow: hidden; }
  body { background: var(--bg); position: relative; font-family: "Tinos", serif; color: var(--ink); }

  .label {
    position: absolute; width: 390px; height: 464px;
    border-radius: 50%; background: var(--paper);
    box-shadow: 2px 5px 8px rgba(0,0,0,0.22);
  }
  .label--a { left: 159px; top: 76px; }
  .label--b { left: 648px; top: 80px; }
  .label--c { left: 164px; top: 615px; }
  .label--d { left: 648px; top: 620px; }

  .face {
    position: absolute; inset: 11px; border-radius: 50%; overflow: hidden;
  }
  .honeycomb-field {
    position: absolute; left: 0; right: 0; top: 280px; bottom: 0;
    background: linear-gradient(to bottom, var(--paper) 0%, var(--lemon-soft) 100%);
    opacity: 0.8;
  }
  .band {
    position: absolute; left: -10px; right: -10px; top: 272px; height: 0;
  }
  .ring {
    position: absolute; inset: 9px; border-radius: 50%;
    border: 5px solid var(--lemon); pointer-events: none;
  }

  .brand {
    position: absolute; left: 0; right: 0; top: 80px;
    display: flex; align-items: center; justify-content: center; gap: 8px;
  }
  .brand-mark { width: 22px; height: 22px; background: var(--lemon); }
  .brand-name { font-family: "Tinos", serif; font-size: 26px; color: var(--ink); }

  .title-band {
    position: absolute; left: 0; right: 0; top: 206px; height: 86px;
    background: var(--lemon); text-align: center;
  }
  .title-kicker {
    display: block; font-family: "Tinos", serif; font-size: 28px;
    letter-spacing: 6px; line-height: 1; margin-top: 7px; color: var(--ink);
  }
  .title-main { display: block; line-height: 1; color: var(--ink); white-space: nowrap; }
  .title-main--caps { font-family: "Federo", sans-serif; font-size: 44px; text-transform: uppercase; letter-spacing: -1px; }
  .title-main--script { font-family: "Federo", sans-serif; font-size: 48px; }
  .title-main--bold { font-family: "Fraunces", serif; font-weight: 700; font-size: 45px; }
  .title-main--display { font-family: "DM Serif Display", serif; font-size: 48px; }

  .details {
    position: absolute; left: 0; right: 0; top: 318px;
    text-align: center; font-size: 16px; line-height: 20px; color: var(--ink);
  }

  .size-note {
    position: absolute; left: 0; right: 0; top: 1120px; text-align: center;
    font-family: "Lexend", sans-serif; color: var(--ink-dark);
  }
  .size-note .num { font-size: 46px; font-weight: 700; }
  .size-note .unit { font-size: 32px; font-weight: 600; }
</style>
</head>
<body>

  <section class="label label--a">
    <div class="face"><div class="honeycomb-field" role="img" aria-label="Faint honeycomb pattern"></div></div>
    <div class="ring"></div>
    <div class="brand"><span class="brand-mark"></span><span class="brand-name">Meadow Drift</span></div>
    <div class="title-band">
      <span class="title-kicker">GOURMET</span>
      <span class="title-main title-main--caps">Candied Pecans</span>
    </div>
    <p class="details">Made with Cinnamon, Brown Sugar &amp; Salt<br>Order More @ (555) 014-2738<br>Meadow Drift Market, LLC</p>
  </section>

  <section class="label label--b">
    <div class="face"><div class="honeycomb-field" role="img" aria-label="Faint honeycomb pattern"></div></div>
    <div class="ring"></div>
    <div class="brand"><span class="brand-mark"></span><span class="brand-name">Meadow Drift</span></div>
    <div class="title-band">
      <span class="title-kicker">GOURMET</span>
      <span class="title-main title-main--script">Candied Pecans</span>
    </div>
    <p class="details">Made with Cinnamon, Brown Sugar &amp; Salt<br>Order More @ (555) 014-2738<br>Meadow Drift Market, LLC</p>
  </section>

  <section class="label label--c">
    <div class="face"><div class="honeycomb-field" role="img" aria-label="Faint honeycomb pattern"></div></div>
    <div class="ring"></div>
    <div class="brand"><span class="brand-mark"></span><span class="brand-name">Meadow Drift</span></div>
    <div class="title-band">
      <span class="title-kicker">GOURMET</span>
      <span class="title-main title-main--bold">Candied Pecans</span>
    </div>
    <p class="details">Made with Cinnamon, Brown Sugar &amp; Salt<br>Order More @ (555) 014-2738<br>Meadow Drift Market, LLC</p>
  </section>

  <section class="label label--d">
    <div class="face"><div class="honeycomb-field" role="img" aria-label="Faint honeycomb pattern"></div></div>
    <div class="ring"></div>
    <div class="brand"><span class="brand-mark"></span><span class="brand-name">Meadow Drift</span></div>
    <div class="title-band">
      <span class="title-kicker">GOURMET</span>
      <span class="title-main title-main--display">Candied Pecans</span>
    </div>
    <p class="details">Made with Cinnamon, Brown Sugar &amp; Salt<br>Order More @ (555) 014-2738<br>Meadow Drift Market, LLC</p>
  </section>

  <p class="size-note"><span class="num">2</span> <span class="unit">in. x</span> <span class="num">2.5</span> <span class="unit">in.</span></p>

</body>
</html>
```